New clean and fresh corporate PPT template for Telecom equipment maker

KVR (VELMAQ KVRT) is a telecom equipment maker in Silicon Valley. Our current PPT template that goes with http://morelintek.com is overbuilt, dark, huge in file size, and looks the opposite of fresh and clean.
Our new microsite @ http://investor-kvrt.com is the direction we want to go. We are B2B, selling to telecom operators, but still want something that looks clean and fresh and not stuffy, hence primarily white background with maximum whitespace in 16:9 format.
Style guidelines attached, exclusive use of approved colors required, the master should remain as simple as possible, and we want the file size to stay reasonable (i.e. less is better). Features we would like include:
- Lato font built-in to the template
- Text boxes with standard size fonts, that automatically get smaller with indention
- An interesting bullet style, nothing crazy, but with visual interest
- A pre-selected table format that is clean and allows for high-density tables with many rows & columns
- Whichever standard slides layouts in the master you think would help result in slides that are found in the current deck, without someone needing to build their own slide

```html
<!DOCTYPE html>
<html lang="en">
<head>
<meta charset="utf-8">
<title>Safe Harbor Statement</title>
<link href="https://fonts.googleapis.com/css2?family=Lato:wght@700;900&family=Arimo:wght@400&display=swap" rel="stylesheet">
<style>
  :root {
    --accent-blue: #3bb3e6;
    --body-ink: #2b2b2b;
    --muted-grey: #c9c9c9;
    --mark-grey: #cfd3d6;
    --page-bg: #ffffff;
  }
  html, body {
    margin: 0;
    padding: 0;
    overflow: hidden;
    background: var(--page-bg);
  }
  .slide {
    position: relative;
    width: 1200px;
    height: 675px;
    overflow: hidden;
    background: var(--page-bg);
  }
  .network-art {
    position: absolute;
  }
  .network-art--top {
    right: 0;
    top: 0;
    width: 295px;
    height: 96px;
    background: radial-gradient(ellipse at 60% 30%, rgba(59,179,230,0.16), rgba(59,179,230,0) 70%);
  }
  .network-art--bottom {
    left: 0;
    bottom: 0;
    width: 290px;
    height: 96px;
    background: radial-gradient(ellipse at 40% 80%, rgba(59,179,230,0.16), rgba(59,179,230,0) 70%);
  }
  .slide-title {
    position: absolute;
    left: 22px;
    top: 10px;
    margin: 0;
    font-family: "Lato", sans-serif;
    font-weight: 900;
    font-size: 57px;
    letter-spacing: -0.3px;
    color: var(--accent-blue);
  }
  .disclaimer {
    position: absolute;
    left: 44px;
    top: 124px;
    width: 1112px;
    margin: 0;
    font-family: "Arimo", Arial, sans-serif;
    font-size: 20.6px;
    line-height: 26.3px;
    text-align: center;
    color: var(--body-ink);
  }
  .footer-note {
    position: absolute;
    left: 0;
    right: 0;
    top: 643px;
    text-align: center;
    font-family: "Arimo", Arial, sans-serif;
    font-size: 18.5px;
    color: var(--muted-grey);
    padding-right: 0;
  }
  .footer-note span {
    position: relative;
    left: 0;
  }
  .brand-tag {
    position: absolute;
    right: 14px;
    top: 636px;
    display: flex;
    align-items: center;
    gap: 8px;
  }
  .brand-name {
    font-family: "Lato", sans-serif;
    font-weight: 900;
    font-size: 28px;
    color: var(--mark-grey);
    letter-spacing: 0.5px;
  }
  .brand-rule {
    width: 2px;
    height: 28px;
    background: var(--mark-grey);
  }
  .page-number {
    font-family: "Lato", sans-serif;
    font-weight: 900;
    font-size: 28px;
    color: var(--accent-blue);
  }
</style>
</head>
<body>
  <div class="slide">
    <div class="network-art network-art--top" role="img" aria-label="Decorative network of connected nodes and lines"></div>
    <div class="network-art network-art--bottom" role="img" aria-label="Decorative network of connected nodes and lines"></div>

    <h1 class="slide-title">Safe Harbor Statement</h1>

    <p class="disclaimer">This presentation contains forward-looking statements that are subject to the safe harbors created under the Securities Act of 1933 and the Securities Exchange Act of 1934.&nbsp; Words such as “anticipate,” “believe,” “continue,” “could,” “estimate,” “expect,” “goal,” “intend,” “may,” “plan,” “project,” “seek,” “should,” “target,” “will,” “would,” variations of such words, and similar expressions are intended to identify forward-looking statements. In addition, forward-looking statements include, among others, statements that refer to financial estimates; projections of revenue, margins, expenses or other financial items. Readers are cautioned that actual results could differ materially from those expressed in or contemplated by the forward-looking statements. Factors that could cause actual results to differ include, but are not limited to, commercial acceptance of the Company's products; intense competition in the communications equipment market; the Company's ability to execute on its strategy and operating plans; and economic conditions specific to the communications, networking, internet and related industries. In addition, please refer to the risk factors contained in the Company's SEC filings available at www.filingsdesk.org, including without limitation, the Company's annual report on Form 10-K and quarterly reports on Forms 10-Q. Readers are cautioned not to place undue reliance on any forward-looking statements, which speak only as of the date on which they are made. The Company undertakes no obligation to update or revise any forward-looking statements for any reason.</p>

    <div class="footer-note"><span>© 2018 Kovar Ridge Solutions – Proprietary and Confidential</span></div>

    <div class="brand-tag">
      <span class="brand-name">KVR</span>
      <span class="brand-rule"></span>
      <span class="page-number">2</span>
    </div>
  </div>
</body>
</html>
```